Booth Backdrop Design- 118"w x 89"h x 13"d

Please visit https://crestvaleprobe.com/ and review the first page and make a booth display that will reflect our brand as the dominant leader in the home inspection industry.
Full Display Size: 118"w x 89"h x 13"d
Assembled Podium Size: 37"w x 40"h x 17.5"d
The booth can be seen here https://www.marbotexhibit.com/10x10ft-standard-trade-show-booth-27.html

The Hex Color will be this -The hex color #0070BB

Please include some variations with all of the image assets provide and some variations that are very close to this FrontofBrochure Close to this for Final attached as an image.

```html
<!DOCTYPE html>
<html lang="en">
<head>
<meta charset="utf-8">
<title>Crestvale Probe – Booth Backdrop and Podium</title>
<link rel="stylesheet" href="https://fonts.googleapis.com/css2?family=Montserrat:wght@500;600;700;800;900&family=Oswald:wght@500;600&display=swap">
<style>
  :root{
    --board:#464646;
    --label:#6b6b6b;
    --number:#595959;
    --brand:#0070bb;
    --brand-deep:#0b5fae;
    --ink:#141414;
    --white:#ffffff;
    --sky-top:#1565b8;
    --sky-mid:#4d88c6;
    --sky-low:#8eacc9;
    --ridge:#6f7f8c;
    --wall:#eee6d8;
    --glow:#e6a84f;
    --foliage:#3f5a3a;
    --stone:#cbbda4;
    --badge-grey:#dfe3e8;
    --badge-navy:#c9d3e3;
    --badge-red:#c8343a;
    --badge-gold:#d6bd6e;
  }
  *{margin:0;padding:0;box-sizing:border-box}
  html,body{width:1063px;height:1200px;overflow:hidden;background:var(--board)}
  body{position:relative;font-family:"Montserrat",sans-serif;color:var(--white)}

  .side-label{position:absolute;font-weight:500;font-size:12px;letter-spacing:1.5px;color:var(--label);white-space:nowrap;transform:translate(-50%,-50%) rotate(-90deg)}
  .side-label--backdrop{left:72px;top:713px}
  .side-label--podium{left:119px;top:1033px}
  .sheet-number{position:absolute;left:970px;top:1126px;font-weight:600;font-size:46px;line-height:1;color:var(--number)}

  .backdrop{position:absolute;left:94px;top:86px;width:874px;height:674px;background:var(--white);overflow:hidden;box-shadow:0 4px 10px rgba(0,0,0,.35)}
  .backdrop__scene{position:absolute;left:0;top:0;width:874px;height:559px;
    background:
      radial-gradient(ellipse 34% 16% at 50% 80%, rgba(230,168,79,.85) 0%, rgba(230,168,79,0) 100%),
      radial-gradient(ellipse 22% 14% at 80% 78%, rgba(230,168,79,.55) 0%, rgba(230,168,79,0) 100%),
      radial-gradient(ellipse 22% 22% at 8% 88%, rgba(63,90,58,.55) 0%, rgba(63,90,58,0) 100%),
      radial-gradient(ellipse 20% 22% at 94% 86%, rgba(63,90,58,.55) 0%, rgba(63,90,58,0) 100%),
      linear-gradient(180deg,var(--sky-top) 0%,#2d76c2 24%,var(--sky-mid) 42%,var(--sky-low) 54%,var(--ridge) 61%,var(--wall) 68%,#e9dcc6 78%,var(--stone) 90%,#8da6b5 100%)}

  .brand-lockup{position:absolute;left:258px;top:29px;display:flex;align-items:center;gap:10px}
  .brand-lockup__mark{width:80px;height:80px;border-radius:50%;border:4px solid var(--white);background:var(--brand-deep);flex:none}
  .brand-lockup__name{font-weight:800;font-size:26px;letter-spacing:.5px;line-height:1;white-space:nowrap}
  .brand-lockup__tag{font-weight:700;font-size:10px;letter-spacing:.4px;margin-top:6px;display:flex;align-items:center;gap:5px;white-space:nowrap}
  .brand-lockup__tag::before,.brand-lockup__tag::after{content:"";height:2px;flex:1;background:var(--white)}

  .headline{position:absolute;left:0;width:874px;top:127px;text-align:center;font-weight:800;font-size:35px;letter-spacing:.5px;line-height:1}
  .headline-box{position:absolute;left:188px;top:169px;width:496px;height:65px;border:2px solid var(--white);border-radius:10px;display:flex;align-items:center;justify-content:center;gap:18px}
  .headline-box__big{font-weight:900;font-size:58px;line-height:1;letter-spacing:-1px}
  .headline-box__small{font-weight:900;font-size:26px;line-height:.95}

  .stats{position:absolute;top:253px;left:280px;display:flex;gap:4px}
  .stat{height:33px;display:flex;align-items:center;gap:8px;padding:0 12px;border-radius:3px}
  .stat--blue{background:var(--brand);width:147px}
  .stat--dark{background:var(--ink);width:160px;padding-left:8px}
  .stat__num{font-family:"Oswald",sans-serif;font-weight:600;font-size:27px;line-height:1}
  .stat__text{font-weight:600;font-size:11px;line-height:1.05}
  .stat__over{font-size:6px;font-weight:600;transform:rotate(-90deg);width:8px}

  .contact-bar{position:absolute;left:160px;top:538px;width:550px;height:38px;display:flex}
  .contact-bar__phone{position:relative;width:268px;background:var(--brand);border-radius:19px 0 0 19px;display:flex;align-items:center;padding-left:48px;font-weight:700;font-size:26px;white-space:nowrap;clip-path:polygon(0 0,100% 0,96% 100%,0 100%)}
  .contact-bar__icon{position:absolute;left:0;top:0;width:38px;height:38px;border-radius:50%;background:var(--ink);border:2px solid var(--white);display:flex;align-items:center;justify-content:center}
  .contact-bar__url{flex:1;background:var(--ink);border-radius:0 19px 19px 0;margin-left:-12px;display:flex;align-items:center;padding-left:30px;font-weight:500;font-size:23px;white-space:nowrap}
  .contact-bar__url b{font-weight:700}

  .credential{position:absolute}
  .credential--rating{left:82px;top:606px;width:103px;height:38px;border-radius:4px;background:var(--badge-grey)}
  .credential--stars{left:212px;top:603px;width:96px;height:42px;border-radius:3px;background:var(--badge-red)}
  .credential--bars{left:333px;top:609px;width:117px;height:32px;border-radius:3px;background:var(--badge-navy)}
  .credential-divider{position:absolute;left:466px;top:603px;width:1px;height:47px;background:#7a7a7a}
  .credential--realtors{left:482px;top:609px;width:89px;height:36px;border-radius:3px;background:var(--badge-navy)}
  .credential--seal-gold{left:593px;top:596px;width:55px;height:55px;border-radius:50%;background:var(--badge-gold)}
  .credential--seal-red{left:666px;top:596px;width:55px;height:55px;border-radius:50%;background:var(--badge-red)}
  .credential--infrared{left:744px;top:596px;width:40px;height:40px;border-radius:50%;background:var(--badge-grey)}

  .podium{position:absolute;left:141px;top:816px;width:787px;height:247px;background:var(--brand);box-shadow:0 4px 10px rgba(0,0,0,.35)}
  .podium__fold{position:absolute;top:0;height:247px;border-left:1px dashed rgba(255,255,255,.35)}
  .podium__side-url{position:absolute;top:124px;font-weight:500;font-size:11px;transform:translate(-50%,-50%) rotate(-90deg);white-space:nowrap}
  .podium__side-url b{font-weight:700}
  .podium__lockup{position:absolute;left:0;width:787px;top:67px;text-align:center}
  .podium__mark{width:50px;height:50px;border-radius:50%;border:3px solid var(--white);background:var(--brand-deep);margin:0 auto 9px}
  .podium__name{font-weight:800;font-size:14px;letter-spacing:.4px;line-height:1}
  .podium__tag{font-weight:700;font-size:5.5px;letter-spacing:.3px;margin-top:3px;display:flex;justify-content:center;align-items:center;gap:4px}
  .podium__tag::before,.podium__tag::after{content:"";height:1px;width:22px;background:var(--white)}
  .podium__url{position:absolute;left:0;width:787px;top:186px;text-align:center;font-weight:500;font-size:14px}
  .podium__url b{font-weight:700}
</style>
</head>
<body>
  <div class="side-label side-label--backdrop">BACKDROP</div>
  <div class="side-label side-label--podium">PODIUM</div>

  <section class="backdrop">
    <div class="backdrop__scene" role="img" aria-label="Evening view of a white Spanish-style home with terracotta roof, warmly lit covered patio, palm trees, mountains and a pool under a blue sky"></div>

    <div class="brand-lockup">
      <div class="brand-lockup__mark"></div>
      <div>
        <div class="brand-lockup__name">CRESTVALE PROBE</div>
        <div class="brand-lockup__tag">INSPECTION PROFESSIONALS</div>
      </div>
    </div>

    <h1 class="headline">SOUTHERN CALIFORNIA’S</h1>
    <div class="headline-box">
      <span class="headline-box__big">#1 HOME</span>
      <span class="headline-box__small">INSPECTION<br>COMPANY</span>
    </div>

    <div class="stats">
      <div class="stat stat--blue"><span class="stat__num">65+</span><span class="stat__text">CERTIFIED<br>INSPECTORS</span></div>
      <div class="stat stat--dark"><span class="stat__over">OVER</span><span class="stat__num">600K</span><span class="stat__text">HOMES<br>INSPECTED!</span></div>
    </div>

    <div class="contact-bar">
      <div class="contact-bar__phone">
        <span class="contact-bar__icon">
          <svg width="20" height="20" viewBox="0 0 24 24" aria-hidden="true"><path fill="#fff" d="M6.6 10.8a15 15 0 0 0 6.6 6.6l2.2-2.2a1 1 0 0 1 1-.25 11.4 11.4 0 0 0 3.6.57 1 1 0 0 1 1 1V20a1 1 0 0 1-1 1A17 17 0 0 1 3 4a1 1 0 0 1 1-1h3.5a1 1 0 0 1 1 1c0 1.25.2 2.45.57 3.57a1 1 0 0 1-.25 1z"/></svg>
        </span>
        (866) 555-0142
      </div>
      <div class="contact-bar__url"><b>crestvaleprobe</b>.com</div>
    </div>

    <div class="credential credential--rating"></div>
    <div class="credential credential--stars"></div>
    <div class="credential credential--bars"></div>
    <div class="credential-divider"></div>
    <div class="credential credential--realtors"></div>
    <div class="credential credential--seal-gold"></div>
    <div class="credential credential--seal-red"></div>
    <div class="credential credential--infrared"></div>
  </section>

  <section class="podium">
    <div class="podium__fold" style="left:148px"></div>
    <div class="podium__fold" style="left:250px"></div>
    <div class="podium__fold" style="left:538px"></div>
    <div class="podium__fold" style="left:640px"></div>
    <div class="podium__side-url" style="left:199px">www.<b>crestvaleprobe</b>.com</div>
    <div class="podium__side-url" style="left:589px">www.<b>crestvaleprobe</b>.com</div>
    <div class="podium__lockup">
      <div class="podium__mark"></div>
      <div class="podium__name">CRESTVALE PROBE</div>
      <div class="podium__tag">INSPECTION PROFESSIONALS</div>
    </div>
    <div class="podium__url">www.<b>crestvaleprobe</b>.com</div>
  </section>

  <div class="sheet-number">01</div>
</body>
</html>
```